Introductory Postcard

We need 2 introductory postcard designed. We're a new foundation. We're mailing these postcards to potential sponsors and business partners. You can go to our website "lanternpathway.org" for a briefing of our foundation. When using my logo please delete Inc. We want to introduce our foundation and give them a few reasons why they should be a part of it.

Target Market(s)

Potential sponsors and business partners. We are looking for monetary and brand new shoe support. We're looking to build up shoe inventory so we need shoes. We're willing to purchase shoes as well.

Industry/Entity Type

Business

Requirements
Must have
• The same color scheme as the website. 1st postcard should target shoe stores. We need brand new shoe inventory, so shoe stores are a target. 2nd postcard should target professional sponsors such as lawyers, doctors, dentist, etc.
Should not have
• Nothing over the top. Postcard should be clean, simple, and informative.

```html
<!DOCTYPE html>
<html lang="en">
<head>
<meta charset="utf-8">
<title>Lantern Pathway Foundation – Introductory Postcards</title>
<link rel="stylesheet" href="https://fonts.googleapis.com/css2?family=Tinos:wght@400;700&display=swap">
<style>
  :root {
    --page-bg: #9b9b9b;
    --card-bg: #ffffff;
    --brand-red: #ee0000;
    --ink-black: #050505;
    --ink-white: #ffffff;
    --header-grey: #ececec;
    --rule-dark: #2a2a2a;
    --badge-grey: #c9c9c9;
    --pay-blue: #1b3f8f;
  }
  * { box-sizing: border-box; margin: 0; padding: 0; }
  html, body {
    width: 809px; height: 1200px; overflow: hidden;
    background: var(--page-bg);
    font-family: "Tinos", "Times New Roman", serif;
  }
  .canvas { position: relative; width: 809px; height: 1200px; }

  .postcard {
    position: absolute; left: 65px; width: 685px; height: 526px;
    background: var(--card-bg);
  }
  .postcard--stores { top: 47px; }
  .postcard--professionals { top: 616px; }

  .postcard__header {
    position: absolute; left: 9px; top: 9px; width: 667px; height: 75px;
    background: linear-gradient(180deg, #f4f4f4, var(--header-grey));
  }
  .brand {
    position: absolute; left: 14px; top: 24px;
    display: flex; align-items: center; gap: 8px;
    color: var(--ink-black); font-size: 19px; font-weight: 700;
  }
  .brand__dot { width: 22px; height: 22px; border-radius: 50%; background: var(--brand-red); }

  .stamp-box {
    position: absolute; left: 582px; top: 17px; width: 80px; height: 84px;
    border: 3px solid var(--rule-dark); z-index: 2;
  }

  .tagline {
    position: absolute; left: 9px; top: 84px; width: 667px; height: 24px;
    background: var(--brand-red); color: var(--ink-white);
    font-size: 15px; line-height: 24px; padding-left: 12px; letter-spacing: 0.2px;
  }

  .story {
    position: absolute; left: 9px; top: 108px; width: 333px; height: 370px;
    background: var(--ink-black); color: var(--ink-white);
  }
  .story__text {
    position: absolute; left: 12px; width: 292px;
    font-size: 15.5px; line-height: 28px; text-transform: uppercase;
  }
  .story__text--top { top: 6px; }
  .story__text--bottom { top: 304px; }
  .story__photos {
    position: absolute; left: 0; top: 119px; width: 316px; height: 175px; display: flex;
  }
  .photo { height: 100%; }
  .photo--child { width: 136px; background: linear-gradient(135deg, #8a8a8a, #d9d9d9); }
  .photo--sneaker { width: 180px; background: linear-gradient(135deg, #f2f2f2, #6d6d6d); }
  .photo--sneaker-art {
    width: 316px;
    background: linear-gradient(120deg, #f1f1f1 0%, #f2c6de 35%, #e8e8e8 60%, #4a4a4a 100%);
  }
  .story__corner { position: absolute; left: 0; bottom: 0; }

  .invite {
    position: absolute; left: 342px; top: 108px; width: 334px; height: 196px;
    background: var(--ink-black); color: var(--ink-white);
    text-align: center; font-size: 24px; line-height: 35px; padding-top: 10px;
  }

  .address-lines {
    position: absolute; left: 360px; top: 356px; width: 302px;
  }
  .address-lines span {
    display: block; height: 28px; border-bottom: 2px solid var(--rule-dark);
  }
  .address-lines span:first-child { height: 0; }

  .footer {
    position: absolute; left: 9px; top: 478px; width: 667px; height: 39px;
  }
  .footer__web {
    position: absolute; left: 0; top: 0; width: 442px; height: 39px;
    background: var(--brand-red); color: var(--ink-white);
    font-size: 17px; line-height: 39px; padding-left: 42px;
  }
  .payments {
    position: absolute; right: 8px; top: 11px; display: flex; align-items: center; gap: 5px;
  }
  .payments__name { color: var(--pay-blue); font-size: 15px; font-weight: 700; margin-right: 4px; }
  .payments__badge { width: 30px; height: 19px; background: var(--badge-grey); border-radius: 2px; }
</style>
</head>
<body>
<main class="canvas">

  <!-- Postcard 1: shoe stores -->
  <article class="postcard postcard--stores">
    <header class="postcard__header">
      <div class="brand"><span class="brand__dot"></span>Lantern Pathway Foundation</div>
    </header>
    <div class="stamp-box"></div>
    <p class="tagline">REBUILDING LIVES ONE STEP AT A TIME...</p>

    <section class="story">
      <p class="story__text story__text--top">New shoes build confidence, health and hope. Help us put brand new shoes on children in need.</p>
      <div class="story__photos">
        <div class="photo photo--child" role="img" aria-label="Black and white photo of a smiling young girl"></div>
        <div class="photo photo--sneaker" role="img" aria-label="Black and white photo of a canvas sneaker"></div>
      </div>
      <p class="story__text story__text--bottom">We accept donations and we also buy inventory.</p>
      <svg class="story__corner" width="32" height="36" viewBox="0 0 32 36" aria-hidden="true"><polygon points="0,0 32,36 0,36" fill="#ee0000"/></svg>
    </section>

    <section class="invite">
      SHOE STORES:<br>PARTNER WITH US<br>DONATE OR SELL<br>BRAND NEW SHOES<br>TO OUR FOUNDATION
    </section>

    <div class="address-lines"><span></span><span></span><span></span><span></span></div>

    <footer class="footer">
      <p class="footer__web">lanternpathway.org</p>
      <div class="payments">
        <span class="payments__name">PayLink</span>
        <span class="payments__badge"></span><span class="payments__badge"></span>
        <span class="payments__badge"></span><span class="payments__badge"></span>
      </div>
    </footer>
  </article>

  <!-- Postcard 2: professional sponsors -->
  <article class="postcard postcard--professionals">
    <header class="postcard__header">
      <div class="brand"><span class="brand__dot"></span>Lantern Pathway Foundation</div>
    </header>
    <div class="stamp-box"></div>
    <p class="tagline">REBUILDING LIVES ONE STEP AT A TIME...</p>

    <section class="story">
      <p class="story__text story__text--top">Sponsors fund brand new shoes for families in need and show clients their practice gives back.</p>
      <div class="story__photos">
        <div class="photo photo--sneaker-art" role="img" aria-label="Canvas sneakers with pink floral swirls on a light background"></div>
      </div>
      <p class="story__text story__text--bottom">A gift of any size puts a child on new footing.</p>
      <svg class="story__corner" width="32" height="36" viewBox="0 0 32 36" aria-hidden="true"><polygon points="0,0 32,36 0,36" fill="#ee0000"/></svg>
    </section>

    <section class="invite">
      BECOME A SPONSOR<br>LAWYERS, DOCTORS<br>AND DENTISTS:<br>YOUR SUPPORT BUYS<br>NEW SHOES FOR KIDS
    </section>

    <div class="address-lines"><span></span><span></span><span></span><span></span></div>

    <footer class="footer">
      <p class="footer__web">lanternpathway.org</p>
      <div class="payments">
        <span class="payments__name">PayLink</span>
        <span class="payments__badge"></span><span class="payments__badge"></span>
        <span class="payments__badge"></span><span class="payments__badge"></span>
      </div>
    </footer>
  </article>

</main>
</body>
</html>
```